Brightivo sanitzing wipes: logo, inner foil 6*8cm and consumer carton

we need a clever but simple logo design for a product and integrated look for the packaging (inner foil 6*8 cm and consumer carton). texts are provided for each and some examples of other products and formatting. we would use very simple imagery and color schemes. the main theme is safety, convenience, utility.

for the winning design we will for sure have some changes and adaptations and i would pay additionally for those.

Target Market(s)

American and European retail mass merchants -- wholesale stores, online, retail

Industry/Entity Type

Health And Wellness

Font styles to use
Sans Serif

Requirements
Must have
• Correct formatting of texts in accordance to regulations. Clear communication of texts in an easy to read and understandable formatting. Engaging, but simple design.
Nice to have
• Interesting use of color and contrast. some decent imagery/visual graphics that can make the outter packaging pop on shelf.
Should not have
• odd fonts or formatting. knock-offs of other designs of a similar product in its category, cliché or overused imagery

```html
<!DOCTYPE html>
<html lang="en">
<head>
<meta charset="UTF-8">
<title>Brightivo Sanitizing Hand Wipes – Foil Sachet</title>
<link href="https://fonts.googleapis.com/css2?family=Montserrat:wght@300;400;600;700;800&family=Open+Sans:wght@400;600;700&display=swap" rel="stylesheet">
<style>
  :root{
    --bg:#ffffff;
    --foil-silver:#e4e8ec;
    --foil-silver-light:#f4f6f8;
    --foil-blue:#1fb6e6;
    --foil-blue-deep:#0f8fcc;
    --foil-blue-light:#49d0f5;
    --seal-blue:#1aa3dc;
    --teal:#0c7f9a;
    --brand-green:#3aa64a;
    --pill-green:#38a83d;
    --pill-red:#d42b2b;
    --white:#ffffff;
    --grey-text:#5f6b73;
  }
  *{box-sizing:border-box;margin:0;padding:0}
  html,body{width:1200px;height:960px;overflow:hidden;background:var(--bg)}
  body{font-family:"Open Sans",Arial,sans-serif;position:relative}

  .sachet{
    position:absolute;top:250px;width:550px;height:440px;border-radius:6px;
    padding:22px;
  }
  .sachet--front{left:35px;
    background:linear-gradient(180deg,var(--foil-silver-light) 0%,var(--foil-silver) 35%,#bfe6f3 62%,var(--foil-blue-light) 82%,var(--foil-blue) 100%);}
  .sachet--back{left:615px;
    background:linear-gradient(180deg,var(--foil-blue-deep) 0%,var(--foil-blue) 50%,var(--foil-blue-light) 100%);}
  .seal-lines{position:absolute;inset:0;pointer-events:none}
  .panel{position:relative;width:100%;height:100%;padding:22px 28px}

  .sku{position:absolute;left:4px;top:60px;font-size:11px;color:var(--grey-text);
    transform:rotate(-90deg);transform-origin:left top;}

  .brand{display:flex;align-items:center;gap:10px}
  .brand__name{font-family:"Montserrat",Arial,sans-serif;font-weight:300;font-size:46px;letter-spacing:1px;color:var(--brand-green)}
  .brand__dot{width:14px;height:14px;border-radius:50%;background:var(--brand-green)}
  .sachet--back .brand__name{color:var(--white);font-size:34px}
  .sachet--back .brand__dot{background:var(--white);width:11px;height:11px}

  .product{font-family:"Montserrat",Arial,sans-serif;color:var(--teal);margin-top:2px;line-height:1.05}
  .product__main{font-weight:800;font-size:24px;letter-spacing:.5px}
  .product__sub{font-weight:400;font-size:22px;letter-spacing:2px}
  .sachet--back .product{color:var(--white)}
  .sachet--back .product__main{font-size:17px}
  .sachet--back .product__sub{font-size:15px}

  .claims{position:absolute;left:250px;top:118px;display:flex;flex-direction:column;gap:7px}
  .pill{font-family:"Open Sans",Arial,sans-serif;font-weight:600;font-size:15px;color:var(--white);
    padding:4px 16px;border-radius:6px;border:2px solid rgba(255,255,255,.85);width:max-content}
  .pill--red{background:var(--pill-red);margin-bottom:4px}
  .pill--green{background:var(--pill-green);margin-left:30px;min-width:170px}

  .size{position:absolute;left:28px;bottom:24px;font-family:"Open Sans",Arial,sans-serif;
    font-weight:700;font-size:17px;color:var(--white);line-height:1.25}
  .size span{display:block;padding-left:52px}

  .facts-head{display:flex;justify-content:space-between;align-items:flex-end}
  .purpose{text-align:right;color:var(--white);font-family:"Montserrat",Arial,sans-serif;
    border-top:2px solid var(--white);padding-top:4px;min-width:150px}
  .purpose__label{font-weight:700;font-size:13px}
  .purpose__value{font-weight:400;font-size:13px}
  .facts{color:var(--white);margin-top:10px;font-size:10.5px;line-height:1.45}
  .facts__title{font-family:"Montserrat",Arial,sans-serif;font-weight:800;font-size:24px;
    border-bottom:2px solid var(--white);padding-bottom:3px;margin-bottom:5px}
  .facts h3{font-family:"Montserrat",Arial,sans-serif;font-size:11.5px;font-weight:700;margin-top:4px}
  .facts p{padding-left:20px}
</style>
</head>
<body>

<section class="sachet sachet--front" aria-label="Sachet front">
  <svg class="seal-lines" width="550" height="440" viewBox="0 0 550 440" aria-hidden="true">
    <g fill="none" stroke="rgba(255,255,255,.6)" stroke-width="1.5">
      <rect x="6" y="6" width="538" height="428" rx="4"/>
      <rect x="11" y="11" width="528" height="418" rx="4"/>
      <rect x="16" y="16" width="518" height="408" rx="4"/>
    </g>
  </svg>
  <div class="panel">
    <div class="sku">#06486</div>
    <div class="brand"><span class="brand__dot"></span><span class="brand__name">Brightivo</span></div>
    <div class="product">
      <div class="product__main">SANITIZING HAND</div>
      <div class="product__sub">WIPES</div>
    </div>
    <div class="claims">
      <div class="pill pill--red">Kills 99.99% of Germs</div>
      <div class="pill pill--green">70% alcohol</div>
      <div class="pill pill--green">Fragrance free</div>
      <div class="pill pill--green">Paraben free</div>
      <div class="pill pill--green">Phthalate Free</div>
    </div>
    <div class="size">One Wipe: (5.5" X 7.1")<span>14cm*18cm</span></div>
  </div>
</section>

<section class="sachet sachet--back" aria-label="Sachet back">
  <svg class="seal-lines" width="550" height="440" viewBox="0 0 550 440" aria-hidden="true">
    <g fill="none" stroke="rgba(255,255,255,.45)" stroke-width="1.5">
      <rect x="6" y="6" width="538" height="428" rx="4"/>
      <rect x="11" y="11" width="528" height="418" rx="4"/>
      <rect x="16" y="16" width="518" height="408" rx="4"/>
    </g>
  </svg>
  <div class="panel">
    <div class="facts-head">
      <div>
        <div class="brand"><span class="brand__dot"></span><span class="brand__name">Brightivo</span></div>
        <div class="product">
          <div class="product__main">SANITIZING HAND</div>
          <div class="product__sub">WIPES</div>
        </div>
      </div>
      <div class="purpose">
        <div class="purpose__label">Purpose</div>
        <div class="purpose__value">Antimicrobial</div>
      </div>
    </div>
    <div class="facts">
      <div class="facts__title">Drug facts</div>
      <h3>Active Ingredient</h3>
      <p>Ethyl Alcohol 70%</p>
      <h3>Use</h3>
      <p>• Hand sanitizer</p>
      <h3>Warnings:</h3>
      <p>flammable, keep away from fire or flame. for external use only, do not use on eyes or if you are allergic to any ingredients. If eye contact occurs, rinse thoroughly with water. keep away from children. stop use and ask a doctor should irritation or redness appear and persist for 72 hours. If swallowed, seek medical help or call the Poison Control center right away.</p>
      <h3>Directions:</h3>
      <p>Wipe Hands, Discard (Do Not Flush).</p>
    </div>
  </div>
</section>

</body>
</html>
```